Premium modern eliquids labels 84.5 x 80 mm

I am looking for modern graphics for the labels of a new eliquid line that will have 4 different types of eliquids. It will have a tobacco one (brown colours maybe), a fruity one (bright colours maybe), a minty one (green colours maybe) and a creamy one (beige colours maybe).
I will need one of them to see how the design is, that design will have to be adapted to the other 3 colours of the label.
The brand logo is attached. I also attached a sample of what is mandatory to write on the label, you can change size, place and font of what is written, the only thing that cannot be reduced is the yellow parts. I attach the bottle that we will use.The size of the label is 84.5 x 80 mm (base x height).

Target Market(s)

vapers

Requirements
Must have
• My project must have one of the labels.

```html
<!DOCTYPE html>
<html lang="it">
<head>
<meta charset="utf-8">
<title>Vertex Blend – etichette</title>
<link rel="stylesheet" href="https://fonts.googleapis.com/css2?family=Righteous&family=Roboto+Condensed:wght@400;700&display=swap">
<style>
  :root{
    --page:#ffffff;
    --yellow:#f7c531;
    --ink:#1c1c1c;
    --tob-1:#d9a566; --tob-2:#b5733c; --tob-3:#7a3f12; --tob-text:#f6e8cc;
    --fru-1:#f7d24a; --fru-2:#d44a8a; --fru-3:#5a3d8c; --fru-4:#8fbf5a; --fru-text:#2d2238;
    --min-1:#b6ecd0; --min-2:#6fcf9c; --min-3:#2f9a64; --min-text:#1d5436;
    --cre-1:#fbf5dc; --cre-2:#efe2ae; --cre-3:#d9c78a; --cre-text:#857a5a;
  }
  *{box-sizing:border-box;margin:0;padding:0}
  html,body{width:1200px;height:961px;overflow:hidden;background:var(--page)}
  body{position:relative;font-family:"Roboto Condensed",sans-serif}

  .label{position:absolute;width:423px;height:400px;overflow:hidden;outline:1px solid rgba(0,0,0,.35)}
  .label--tobacco{left:292px;top:71px}
  .label--fruit{left:733px;top:71px}
  .label--mint{left:292px;top:502px}
  .label--cream{left:733px;top:502px}

  .label__art{position:absolute;inset:0}
  .label--tobacco .label__art{background:linear-gradient(135deg,var(--tob-2) 0%,var(--tob-1) 40%,var(--tob-2) 70%,var(--tob-3) 100%)}
  .label--fruit .label__art{background:linear-gradient(135deg,var(--fru-4) 0%,var(--fru-2) 30%,var(--fru-1) 55%,var(--fru-3) 80%,var(--fru-2) 100%)}
  .label--mint .label__art{background:linear-gradient(135deg,var(--min-2) 0%,var(--min-1) 45%,var(--min-2) 75%,var(--min-3) 100%)}
  .label--cream .label__art{background:linear-gradient(135deg,var(--cre-2) 0%,var(--cre-1) 45%,var(--cre-2) 75%,var(--cre-3) 100%)}

  .brand{position:absolute;left:212px;top:180px;transform:translate(-50%,-50%) rotate(-90deg);white-space:nowrap;
    font-family:"Righteous",sans-serif;font-size:30px;letter-spacing:1px}
  .flavour{position:absolute;left:212px;top:336px;transform:translateX(-50%);font-family:"Righteous",sans-serif;font-size:26px;letter-spacing:.5px;white-space:nowrap}
  .volume{position:absolute;left:212px;top:374px;transform:translateX(-50%);font-family:"Righteous",sans-serif;font-size:14px;white-space:nowrap}

  .label--tobacco .brand,.label--tobacco .flavour,.label--tobacco .volume{color:var(--tob-text)}
  .label--fruit .brand,.label--fruit .flavour,.label--fruit .volume{color:var(--fru-text)}
  .label--mint .brand,.label--mint .flavour,.label--mint .volume{color:var(--min-text)}
  .label--cream .brand,.label--cream .flavour,.label--cream .volume{color:var(--cre-text)}

  .legal{position:absolute;left:8px;bottom:8px;width:380px;transform-origin:0 100%;transform:rotate(-90deg) translateY(100%);
    font-size:7.2px;line-height:9.4px;color:var(--ink)}
  .legal b{font-weight:700}
  .legal--right{left:382px;top:255px;bottom:auto;width:240px;white-space:nowrap;
    transform-origin:0 0;transform:rotate(-90deg)}

  .recycle{position:absolute;right:8px;top:280px;display:flex;flex-direction:column;gap:10px;width:60px}
  .recycle__group{display:flex;flex-direction:column;align-items:flex-start;gap:2px}
  .tag{background:var(--yellow);color:var(--ink);font-weight:700;font-size:10px;line-height:10px;padding:1px 3px;text-transform:uppercase}
  .tag--small{font-size:7px;line-height:8px;background:transparent;color:var(--ink);padding:0 3px}
  .tag--code{font-size:12px;line-height:14px;padding:1px 5px;margin-top:2px}

  .bottle-label{position:absolute;left:39px;top:329px;width:186px;height:563px;overflow:hidden;border-radius:4px;
    background:linear-gradient(160deg,var(--tob-2) 0%,var(--tob-1) 35%,var(--tob-2) 65%,var(--tob-3) 100%)}
  .bottle-label .brand{left:93px;top:230px;font-size:40px;color:var(--tob-text)}
  .bottle-label .flavour{left:93px;top:472px;font-size:34px;color:var(--tob-text)}
  .bottle-label .volume{left:93px;top:522px;font-size:18px;color:var(--tob-text)}
</style>
</head>
<body>

<section class="bottle-label">
  <div class="label__art" role="img" aria-label="Motivo astratto di nastri e cerchi in toni marroni del tabacco"></div>
  <p class="brand">VERTEX BLEND</p>
  <p class="flavour">TOBACCO</p>
  <p class="volume">20 ML NET</p>
</section>

<section class="label label--tobacco">
  <div class="label__art" role="img" aria-label="Motivo astratto di nastri e cerchi in toni marroni"></div>
  <p class="legal">L SH20 - 001-PES-D PROD 22-04-2022 D SC 21-04-2024 <b>ISTRUZIONI D'USO:</b> Agitare bene prima dell'utilizzo<br><b>INGREDIENTI:</b> GLICOLE PROPILENICO SOSTANZE AROMATIZZANTI &nbsp; Diluire nelle percentuali consigliate sul nostro sito.<br>Conservare in luogo fresco e asciutto</p>
  <p class="legal legal--right">PRODOTTO E CONFEZIONATO DA lumen srl Via Solari 18 10100 Città<br>P.I 00000000000 Tel. +39 000 0000000 info@vertexblend.test</p>
  <p class="brand">VERTEX BLEND</p>
  <p class="flavour">TOBACCO</p>
  <p class="volume">20 ML NET</p>
  <div class="recycle">
    <div class="recycle__group"><span class="tag">Raccolta<br>plastica</span><span class="tag tag--small">Etichetta</span><span class="tag tag--code">PAP 5</span></div>
    <div class="recycle__group"><span class="tag">Raccolta<br>plastica</span><span class="tag tag--small">Flacone</span><span class="tag tag--code">PET 1</span></div>
  </div>
</section>

<section class="label label--fruit">
  <div class="label__art" role="img" aria-label="Motivo astratto di nastri e cerchi in colori vivaci della frutta"></div>
  <p class="legal">L SH20 - 001-PES-D PROD 22-04-2022 D SC 21-04-2024 <b>ISTRUZIONI D'USO:</b> Agitare bene prima dell'utilizzo<br><b>INGREDIENTI:</b> GLICOLE PROPILENICO SOSTANZE AROMATIZZANTI &nbsp; Diluire nelle percentuali consigliate sul nostro sito.<br>Conservare in luogo fresco e asciutto</p>
  <p class="legal legal--right">PRODOTTO E CONFEZIONATO DA lumen srl Via Solari 18 10100 Città<br>P.I 00000000000 Tel. +39 000 0000000 info@vertexblend.test</p>
  <p class="brand">VERTEX BLEND</p>
  <p class="flavour">FRUIT</p>
  <p class="volume">20 ML NET</p>
  <div class="recycle">
    <div class="recycle__group"><span class="tag">Raccolta<br>plastica</span><span class="tag tag--small">Etichetta</span><span class="tag tag--code">PAP 5</span></div>
    <div class="recycle__group"><span class="tag">Raccolta<br>plastica</span><span class="tag tag--small">Flacone</span><span class="tag tag--code">PET 1</span></div>
  </div>
</section>

<section class="label label--mint">
  <div class="label__art" role="img" aria-label="Motivo astratto di nastri e cerchi in toni verdi menta"></div>
  <p class="legal">L SH20 - 001-PES-D PROD 22-04-2022 D SC 21-04-2024 <b>ISTRUZIONI D'USO:</b> Agitare bene prima dell'utilizzo<br><b>INGREDIENTI:</b> GLICOLE PROPILENICO SOSTANZE AROMATIZZANTI &nbsp; Diluire nelle percentuali consigliate sul nostro sito.<br>Conservare in luogo fresco e asciutto</p>
  <p class="legal legal--right">PRODOTTO E CONFEZIONATO DA lumen srl Via Solari 18 10100 Città<br>P.I 00000000000 Tel. +39 000 0000000 info@vertexblend.test</p>
  <p class="brand">VERTEX BLEND</p>
  <p class="flavour">MINT</p>
  <p class="volume">20 ML NET</p>
  <div class="recycle">
    <div class="recycle__group"><span class="tag">Raccolta<br>plastica</span><span class="tag tag--small">Etichetta</span><span class="tag tag--code">PAP 5</span></div>
    <div class="recycle__group"><span class="tag">Raccolta<br>plastica</span><span class="tag tag--small">Flacone</span><span class="tag tag--code">PET 1</span></div>
  </div>
</section>

<section class="label label--cream">
  <div class="label__art" role="img" aria-label="Motivo astratto di nastri e cerchi in toni beige crema"></div>
  <p class="legal">L SH20 - 001-PES-D PROD 22-04-2022 D SC 21-04-2024 <b>ISTRUZIONI D'USO:</b> Agitare bene prima dell'utilizzo<br><b>INGREDIENTI:</b> GLICOLE PROPILENICO SOSTANZE AROMATIZZANTI &nbsp; Diluire nelle percentuali consigliate sul nostro sito.<br>Conservare in luogo fresco e asciutto</p>
  <p class="legal legal--right">PRODOTTO E CONFEZIONATO DA lumen srl Via Solari 18 10100 Città<br>P.I 00000000000 Tel. +39 000 0000000 info@vertexblend.test</p>
  <p class="brand">VERTEX BLEND</p>
  <p class="flavour">CREAM</p>
  <p class="volume">20 ML NET</p>
  <div class="recycle">
    <div class="recycle__group"><span class="tag">Raccolta<br>plastica</span><span class="tag tag--small">Etichetta</span><span class="tag tag--code">PAP 5</span></div>
    <div class="recycle__group"><span class="tag">Raccolta<br>plastica</span><span class="tag tag--small">Flacone</span><span class="tag tag--code">PET 1</span></div>
  </div>
</section>

</body>
</html>
```